Lantern Marketing Group (LMG)

This is for my business cards. I want a Nice anfd Elegant Business Card to be Designed, Using more or less of the same colors of my logo that i have attached.i would like to have these business cards forever

Thank you

Thank you

Thank you

Contact Information for Business Card

Calvin Ortega
Lantern Marketing Group
C.(555) 482-1306
E-Mail. COrtega@lanternmgroup.example

Font styles to use
Serif
Sans Serif

Colors
d0dfed
cbcbcb
cee9f5

Requirements
Must have
• (LMG)
• Lantern Marketing Group
Nice to have
• 3D affects
Should not have
• Please try not using the flat version of the logo try and use the 3d version please

```html
<!DOCTYPE html>
<html lang="en">
<head>
<meta charset="utf-8">
<title>Lantern Marketing Group – Business Card</title>
<link href="https://fonts.googleapis.com/css2?family=Montserrat:wght@700&family=Open+Sans:wght@400;600;700&display=swap" rel="stylesheet">
<style>
  :root {
    --backdrop: #e9ecef;
    --paper: #ffffff;
    --paper-soft: #f1f3f5;
    --brand-blue: #2f86cc;
    --brand-grey: #6f7378;
    --ink: #2b2e33;
    --night-deep: #0f1822;
    --night-mid: #2a3a4a;
    --band-blue: #6aa3d6;
    --band-grey: #b7bcc2;
    --faint-mark: #d0dfed;
    --mark-light: #cfe3f3;
  }
  * { margin: 0; padding: 0; box-sizing: border-box; }
  html, body { width: 1200px; height: 949px; overflow: hidden; }
  body {
    background: var(--backdrop);
    font-family: "Open Sans", Arial, sans-serif;
    position: relative;
  }
  .card {
    position: absolute;
    width: 525px;
    height: 300px;
    border-radius: 4px;
    box-shadow: 0 14px 30px rgba(0,0,0,.18);
    overflow: hidden;
  }
  .card--front { left: 50px; top: 180px; background: var(--paper); }
  .card--back { left: 625px; top: 470px; background: var(--paper-soft); }

  .wordmark {
    position: absolute;
    font-family: "Montserrat", Arial, sans-serif;
    font-weight: 700;
    text-transform: uppercase;
    letter-spacing: .04em;
    line-height: 1.15;
  }
  .wordmark__square { display: block; }
  .wordmark__name { display: block; }

  .card--front .wordmark {
    left: 0; right: 0; top: 70px;
    display: flex; flex-direction: column; align-items: center; gap: 14px;
    text-align: center;
    color: var(--brand-blue);
    font-size: 26px;
  }
  .card--front .wordmark__square { width: 70px; height: 70px; background: var(--brand-blue); }

  .card-back__art { position: absolute; inset: 0; }
  .card--back .wordmark {
    left: 36px; top: 138px;
    display: flex; align-items: center; gap: 10px;
    color: var(--mark-light);
    font-size: 13px;
  }
  .card--back .wordmark__square { width: 30px; height: 30px; background: var(--mark-light); }

  .faint-mark {
    position: absolute; right: 30px; top: 182px;
    width: 40px; height: 40px;
    background: var(--faint-mark);
  }

  .contact {
    position: absolute; right: 30px; top: 30px;
    text-align: right;
    color: var(--ink);
    font-size: 10.5px;
    line-height: 1.45;
  }
  .contact__name { color: var(--brand-blue); font-weight: 700; font-size: 12px; letter-spacing: .04em; text-transform: uppercase; margin-bottom: 8px; }
  .contact__company { font-weight: 700; text-transform: uppercase; }
  .contact__line { display: flex; justify-content: flex-end; align-items: center; gap: 5px; }
  .contact__gap { height: 8px; }
  .icon { width: 10px; height: 10px; flex: none; }
</style>
</head>
<body>

<section class="card card--front" aria-label="Card front">
  <div class="wordmark">
    <span class="wordmark__square"></span>
    <span class="wordmark__name">Lantern<br>Marketing Group</span>
  </div>
</section>

<section class="card card--back" aria-label="Card back">
  <svg class="card-back__art" viewBox="0 0 525 300" preserveAspectRatio="none" aria-hidden="true">
    <defs>
      <linearGradient id="night" x1="0" y1="0" x2="1" y2="1">
        <stop offset="0" stop-color="#2a3a4a"/>
        <stop offset="1" stop-color="#0f1822"/>
      </linearGradient>
    </defs>
    <path d="M0 0 H205 C230 155 350 245 525 262 V300 H0 Z" fill="url(#night)"/>
    <path d="M205 0 C230 155 350 245 525 262" fill="none" stroke="#b7bcc2" stroke-width="9"/>
    <path d="M216 0 C241 148 358 236 525 251" fill="none" stroke="#6aa3d6" stroke-width="5"/>
  </svg>

  <div class="wordmark">
    <span class="wordmark__square"></span>
    <span class="wordmark__name">Lantern<br>Marketing Group</span>
  </div>

  <div class="faint-mark"></div>

  <div class="contact">
    <p class="contact__name">Calvin Ortega</p>
    <p class="contact__company">Lantern Marketing Group (LMG)</p>
    <p>Suite 123, Street name</p>
    <p>State, Zip 45678, Country</p>
    <div class="contact__gap"></div>
    <p class="contact__line">(555) 482-1306
      <svg class="icon" viewBox="0 0 10 10" aria-hidden="true"><rect x="2.5" y="0.5" width="5" height="9" rx="1" fill="none" stroke="#2f86cc"/></svg>
    </p>
    <p class="contact__line">COrtega@lanternmgroup.example
      <svg class="icon" viewBox="0 0 10 10" aria-hidden="true"><rect x="0.5" y="2" width="9" height="6" fill="#6aa3d6"/><path d="M0.5 2 L5 5.5 L9.5 2" fill="none" stroke="#fff" stroke-width=".8"/></svg>
    </p>
  </div>
</section>

</body>
</html>
```